Bref créative
Brivona Real Estate
Professional
Tom Radcliffe
President
782 W. Hollow Pine Rd. Suite 310
Beverly Hills, CA 90210
tom@BrivonaRealEstate.example
www.BrivonaRealEstate.example
I will upload our logo. If there is a problem with that please use logo on web site www.brivonarealestate.example
Please use our logo.

```html
<!DOCTYPE html>
<html lang="en">
<head>
<meta charset="utf-8">
<title>Brivona Real Estate – Business Card</title>
<link href="https://fonts.googleapis.com/css2?family=Arimo:wght@400;700&display=swap" rel="stylesheet">
<style>
  :root {
    --page: #ffffff;
    --card: #ffffff;
    --card-edge: #d9dadc;
    --card-dark: #8d8f92;
    --navy: #1f3a5f;
    --blue: #2f6aa3;
    --ink: #555a60;
    --soft: #8a8f95;
  }
  * { margin: 0; padding: 0; box-sizing: border-box; }
  html, body { width: 1200px; height: 223px; overflow: hidden; background: var(--page); }
  body { font-family: "Arimo", Arial, sans-serif; position: relative; }

  .card {
    position: absolute; top: 4px; width: 384px; height: 215px;
    background: var(--card); border: 1px solid var(--card-edge);
    box-shadow: 0 1px 3px rgba(0,0,0,.12);
  }
  .card--front { left: 4px; }
  .card--back { left: 408px; }
  .card--dark {
    left: 812px;
    background: linear-gradient(135deg, #9a9c9f, var(--card-dark) 55%, #7f8184);
  }

  .brand { display: flex; align-items: center; gap: 6px; position: absolute; }
  .brand__mark { width: 14px; height: 14px; background: var(--navy); }
  .brand__name {
    font-weight: 700; font-size: 16px; color: var(--navy);
    letter-spacing: .5px; white-space: nowrap;
  }
  .card--front .brand { top: 16px; right: 18px; }
  .card--back .brand,
  .card--dark .brand { top: 50%; left: 50%; transform: translate(-50%, -50%); }
  .card--back .brand__name,
  .card--dark .brand__name { font-size: 19px; }

  .person { position: absolute; left: 14px; top: 96px; }
  .person__name { font-weight: 700; font-size: 13px; color: var(--blue); }
  .person__title { font-size: 9px; color: var(--ink); margin-top: 2px; }

  .contact {
    position: absolute; left: 14px; bottom: 12px;
    font-size: 7.5px; line-height: 11px; color: var(--ink);
  }
</style>
</head>
<body>
  <section class="card card--front">
    <div class="brand">
      <span class="brand__mark"></span>
      <span class="brand__name">Brivona Real Estate</span>
    </div>
    <div class="person">
      <p class="person__name">Tom Radcliffe</p>
      <p class="person__title">President</p>
    </div>
    <div class="contact">
      <p>782 W. Hollow Pine Rd. Suite 310 Beverly Hills, CA 90210</p>
      <p>Cell : 310-555-0142 | Cell : 310-555-0187 | Fax : 888-555-0163</p>
      <p>Email : tom@BrivonaRealEstate.example | Web : www.BrivonaRealEstate.example</p>
    </div>
  </section>

  <section class="card card--back">
    <div class="brand">
      <span class="brand__mark"></span>
      <span class="brand__name">Brivona Real Estate</span>
    </div>
  </section>

  <section class="card card--dark">
    <div class="brand">
      <span class="brand__mark"></span>
      <span class="brand__name">Brivona Real Estate</span>
    </div>
  </section>
</body>
</html>
```